High-end construction company needs a business card design

We need a modern looking business card that draws people in, is memorable and looks so good people will want to sick it on their fridges.
On the first side what is needed are:
Logo
My name - Tomas Verbelk
Title - Managing Director
Website - www.kravel.co.uk
Email - tomas@kravel.co.uk
Telephone - 020 5194 6381
Mobile - 07845319027
On the back side was is needed is a list of all the services we provide:
-Kitchen Renovations
-Bathroom Renovations
-House Renovations
-Garage Conversions
-Extensions
-Loft Conversions
-Conservatories
-Carpentry
-Tiling
-Electrical
-Plumbing & Heating
-Bricklaying
-Landscaping
-Decorating
-Plastering
We would like the colours to be the same shades as on the logo with grey or black for the words.
Target Market(s)
Anyone who needs building work done
Contact Information for Business Card
This business card is for a construction company which strives to deliver excellent service and quality.
The look and feel of the card should represent this.
Requirements
Must have
- On the first side what is needed are:
Logo
My name - Tomas Verbelk
Title - Managing Director
Website - www.kravel.co.uk
Email - tomas@kravel.co.uk
Telephone - 020 5194 6381
Mobile - 07845319027
Nice to have
- Cool looking features

```html
<!DOCTYPE html>
<html lang="en">
<head>
<meta charset="utf-8">
<title>Kravel Construction Ltd — Business Card</title>
<link href="https://fonts.googleapis.com/css2?family=Josefin+Sans:wght@300;400;600;700&display=swap" rel="stylesheet">
<style>
  :root {
    --backdrop: #e9e9e9;
    --card-white: #f1f1f1;
    --forest: #43833b;
    --leaf: #6bb13b;
    --ink-light: #ffffff;
  }
  * { box-sizing: border-box; margin: 0; padding: 0; }
  html, body {
    width: 1200px; height: 1200px; overflow: hidden;
    background: var(--backdrop);
    font-family: "Josefin Sans", Arial, sans-serif;
  }
  .card {
    position: absolute; left: 227px;
    width: 745px; height: 425px;
    border-radius: 30px; overflow: hidden;
  }
  .card--front { top: 135px; background: var(--card-white); }
  .card--back { top: 640px; background: var(--forest); }

  .front-shapes { position: absolute; inset: 0; }

  .brand {
    position: absolute; text-align: center;
    font-weight: 700; line-height: 1;
  }
  .brand__name { display: block; letter-spacing: 2px; }
  .brand__tag { display: block; }
  .card--front .brand { left: 445px; top: 130px; width: 280px; color: var(--leaf); }
  .card--front .brand__name { font-size: 66px; }
  .card--front .brand__tag { font-size: 16px; letter-spacing: 5.5px; margin-top: -5px; }
  .card--back .brand { left: 0; top: 159px; width: 745px; color: var(--ink-light); }
  .card--back .brand__name { font-size: 80px; }
  .card--back .brand__tag { font-size: 19px; letter-spacing: 6.5px; margin-top: -10px; }

  .person { position: absolute; left: 31px; top: 344px; color: var(--ink-light); }
  .person__name { font-size: 25px; font-weight: 600; letter-spacing: 0.5px; }
  .person__title { font-size: 18px; font-weight: 300; margin-top: 6px; letter-spacing: 0.6px; }

  .contacts { position: absolute; left: 236px; top: 298px; list-style: none; color: var(--ink-light); }
  .contacts li {
    display: flex; align-items: center; height: 25px;
    font-size: 18px; font-weight: 300; letter-spacing: 0.3px;
  }
  .contacts svg { width: 18px; height: 18px; margin-right: 13px; flex: none; }

  .services {
    position: absolute; left: 38px; top: 308px; width: 670px;
    color: var(--ink-light); font-size: 18.4px; font-weight: 300;
    line-height: 25px; letter-spacing: 0.2px;
  }
  .services p { text-align: justify; text-align-last: justify; white-space: nowrap; }
</style>
</head>
<body>

<section class="card card--front">
  <svg class="front-shapes" viewBox="0 0 745 425" aria-hidden="true">
    <polygon fill="var(--leaf)" points="0,250 213,122 745,392 745,399 213,140 0,270"/>
    <polygon fill="var(--forest)" points="0,284 213,152 745,404 745,425 0,425"/>
  </svg>

  <div class="brand">
    <span class="brand__name">KRAVEL</span>
    <span class="brand__tag">CONSTRUCTION LTD</span>
  </div>

  <div class="person">
    <p class="person__name">Tomas Verbelk</p>
    <p class="person__title">Managing Director</p>
  </div>

  <ul class="contacts">
    <li>
      <svg viewBox="0 0 18 18" aria-hidden="true"><circle cx="9" cy="9" r="9" fill="#fff"/><path d="M4.5 8 Q9 4 13.5 8 L12 9.5 L10.5 8.5 L7.5 8.5 L6 9.5 Z M6 10.5 H12 V13 H6 Z" fill="var(--forest)"/></svg>
      020 5194 6381
    </li>
    <li>
      <svg viewBox="0 0 18 18" aria-hidden="true"><circle cx="9" cy="9" r="9" fill="#fff"/><rect x="6" y="3.8" width="6" height="10.4" rx="1.2" fill="var(--forest)"/><rect x="7" y="5.2" width="4" height="6.8" fill="#fff"/></svg>
      07845319027
    </li>
    <li>
      <svg viewBox="0 0 18 18" aria-hidden="true"><circle cx="9" cy="9" r="9" fill="#fff"/><rect x="4.5" y="5.8" width="9" height="6.4" fill="none" stroke="var(--forest)" stroke-width="1.3"/><path d="M4.5 5.8 L9 9.6 L13.5 5.8" fill="none" stroke="var(--forest)" stroke-width="1.3"/></svg>
      tomas@kravel.co.uk
    </li>
    <li>
      <svg viewBox="0 0 18 18" aria-hidden="true"><circle cx="9" cy="9" r="9" fill="#fff"/><circle cx="9" cy="9" r="4.8" fill="none" stroke="var(--forest)" stroke-width="1.3"/><path d="M4.2 9 H13.8 M9 4.2 V13.8" stroke="var(--forest)" stroke-width="1.1"/></svg>
      www.kravel.co.uk
    </li>
  </ul>
</section>

<section class="card card--back">
  <div class="brand">
    <span class="brand__name">KRAVEL</span>
    <span class="brand__tag">CONSTRUCTION LTD</span>
  </div>

  <div class="services">
    <p>Kitchen Renovations - Bathroom Renovations - House Renovations - Decorating</p>
    <p>Garage Conversions - Extensions - Loft Conversions - Conservatories - Plastering</p>
    <p>Carpentry - Tiling - Electrical - Plumbing &amp; Heating - Bricklaying -Landscaping</p>
  </div>
</section>

</body>
</html>
```